Business card for Tolvery Anesthesia LLC

This is for a business care for Tolvery Anesthesia LLC. Dr. Lisbeth Tolvery, CRNA, DNAP is the sole provider in the LLC. Business address is 4718 N Brackley Street,
Oakhaven, PA 17342
CRNA stands for certified registered nurse anesthetist
"Keeping you safe and comfortable"
I plan to give this business card to the patients that I provide anesthesia to.
Creative design that ties into Anesthesia. Calm soothing colors.

Target Market(s)

Business card for my patients.

Industry/Entity Type

Medicine

Contact Information for Business Card

Creative, professional, eye catching

Logo Text

Tolvery Anesthesia

Font styles to use
Serif
Script

Colors

Designer to choose colors to be used in the design.

Requirements
Must have
• Tolvery Anesthesia
• Dr. Lisbeth Tolvery, CRNA, DNAP
• tolvery.anesthesia@ quillmail.net
Nice to have
• "Keeping you safe and comfortable"
Should not have
• phone number

```html
<!DOCTYPE html>
<html lang="en">
<head>
<meta charset="utf-8">
<title>Tolvery Anesthesia LLC — Business Card</title>
<link rel="stylesheet" href="https://fonts.googleapis.com/css2?family=Open+Sans:wght@300;400;700&display=swap">
<style>
  :root {
    --backdrop: #0b0f17;
    --paper: #ffffff;
    --brand-blue: #1592f2;
    --brand-deep: #1a84e8;
    --arc-light: #8cc6fb;
    --mark-blue: #4aa8f7;
  }
  * { margin: 0; padding: 0; box-sizing: border-box; }
  html, body {
    width: 1200px; height: 1200px; overflow: hidden;
    background: var(--backdrop);
    font-family: "Open Sans", sans-serif;
  }
  .canvas {
    position: relative; width: 1200px; height: 1200px;
  }
  .card {
    position: absolute; left: 280px;
    width: 640px; height: 380px;
    background: var(--paper);
    overflow: hidden;
  }
  .card--front { top: 150px; }
  .card--back { top: 670px; }

  .wordmark {
    display: flex; flex-direction: column; align-items: center;
    color: var(--brand-deep);
  }
  .wordmark__mark {
    width: 64px; height: 64px; border-radius: 50%;
    background: var(--mark-blue); margin-bottom: 30px;
  }
  .wordmark__name {
    font-weight: 700; font-size: 34px; letter-spacing: 5px; line-height: 1;
  }
  .wordmark__sub {
    font-weight: 300; font-size: 25px; letter-spacing: 2.5px; line-height: 1.2;
  }
  .card--front .wordmark {
    position: absolute; left: 0; right: 0; top: 92px;
  }

  .back__band { position: absolute; inset: 0; }
  .back__info {
    position: absolute; left: 330px; right: 30px; top: 60px;
    display: flex; flex-direction: column; align-items: center;
    color: var(--brand-deep); text-align: center;
  }
  .back__info .wordmark__mark { width: 48px; height: 48px; margin-bottom: 14px; }
  .back__info .wordmark__name { font-size: 26px; letter-spacing: 4px; }
  .back__info .wordmark__sub { font-size: 18px; letter-spacing: 2px; }
  .provider {
    margin-top: 22px; font-weight: 700; font-size: 17px;
  }
  .email { margin-top: 6px; font-weight: 400; font-size: 15px; }
  .tagline {
    margin-top: 34px; font-weight: 300; font-size: 16px; letter-spacing: 1.5px;
    color: var(--brand-blue);
  }
</style>
</head>
<body>
<main class="canvas">
  <section class="card card--front" aria-label="Business card front">
    <div class="wordmark">
      <span class="wordmark__mark" aria-hidden="true"></span>
      <span class="wordmark__name">TOLVERY</span>
      <span class="wordmark__sub">ANESTHESIA LLC.</span>
    </div>
  </section>

  <section class="card card--back" aria-label="Business card back">
    <svg class="back__band" width="640" height="380" viewBox="0 0 640 380" role="img" aria-label="Calm blue band with soft flowing line decoration">
      <path d="M0 0 H470 A430 430 0 0 0 260 380 H0 Z" fill="var(--brand-blue)"/>
      <path d="M470 0 A430 430 0 0 0 260 380" fill="none" stroke="var(--arc-light)" stroke-width="12"/>
    </svg>
    <div class="back__info">
      <span class="wordmark__mark" aria-hidden="true"></span>
      <div class="wordmark">
        <span class="wordmark__name">TOLVERY</span>
        <span class="wordmark__sub">ANESTHESIA LLC.</span>
      </div>
      <p class="provider">Dr. Lisbeth Tolvery, CRNA, DNAP</p>
      <p class="email">tolvery.anesthesia@quillmail.net</p>
      <p class="tagline">Keeping you safe and comfortable</p>
    </div>
  </section>
</main>
</body>
</html>
```